Harbor Notes

I have written a book which I eventually would like to serve a couple of purposes. The initial purpose was to memorialize life events and lessons from my life to pass on to my grandchildren, in hopes they may learn from the experiences. As I completed the book, I now believe I could remove some of the family specific information as much of the information could be useful to many people.

While I want to book to have a great look for the grandkids, more importantly will be the version that we put on the bookshelf to sell. The cover is obviously the first thing a buyer will see and may or may not peak there interest. I would like to include the attached photo as the cover photo and the title language is also attached. Other than that I am not sure what is the best way to design the cover.

```html
<!DOCTYPE html>
<html lang="en">
<head>
<meta charset="utf-8">
<title>Harbor Notes – Book Cover</title>
<link rel="stylesheet" href="https://fonts.googleapis.com/css2?family=Arimo:ital,wght@0,400;0,700;1,700&family=Archivo+Black&display=swap">
<style>
  :root {
    --stage-light: #f2f2f3;
    --stage-dark: #cfd0d2;
    --cover-navy: #14202a;
    --ink-white: #ffffff;
    --photo-warm: #6a4a36;
    --photo-mid: #3b3a3c;
    --photo-cool: #7f8fa8;
  }
  * { box-sizing: border-box; margin: 0; padding: 0; }
  html, body {
    width: 1200px;
    height: 900px;
    overflow: hidden;
  }
  body {
    position: relative;
    background: radial-gradient(ellipse at center, var(--stage-light) 0%, var(--stage-light) 30%, var(--stage-dark) 100%);
    font-family: "Arimo", Arial, sans-serif;
    color: var(--ink-white);
  }
  .book-cover {
    position: absolute;
    left: 366px;
    top: 57px;
    width: 510px;
    height: 776px;
    background: var(--cover-navy);
    overflow: hidden;
  }
  .cover-photo {
    position: absolute;
    left: 0;
    top: 38px;
    width: 100%;
    height: 410px;
    background:
      linear-gradient(to bottom, var(--cover-navy) 0%, rgba(20,32,42,0) 12%, rgba(20,32,42,0) 86%, var(--cover-navy) 100%),
      radial-gradient(ellipse at 55% 65%, var(--photo-cool) 0%, var(--photo-warm) 45%, var(--photo-mid) 100%);
  }
  .greeting {
    position: absolute;
    right: 59px;
    top: 42px;
    font-size: 43px;
    line-height: 1;
    font-weight: 700;
    letter-spacing: 0.5px;
  }
  .grandchildren {
    position: absolute;
    left: 0;
    top: 444px;
    width: 100%;
    text-align: center;
    font-size: 16px;
    font-weight: 700;
    letter-spacing: 1.2px;
    line-height: 24px;
  }
  .tagline {
    position: absolute;
    left: 0;
    top: 508px;
    width: 100%;
    text-align: center;
    font-size: 21px;
    font-weight: 700;
    font-style: italic;
    letter-spacing: 0.3px;
  }
  .title-lead {
    position: absolute;
    right: 272px;
    top: 605px;
    font-size: 27px;
    line-height: 1;
    font-weight: 700;
  }
  .title-word {
    position: absolute;
    left: 245px;
    top: 552px;
    width: 215px;
    height: 80px;
    overflow: visible;
  }
  .title-word text {
    font-family: "Archivo Black", "Arial Black", sans-serif;
    font-size: 110px;
    fill: var(--ink-white);
  }
  .title-aside {
    position: absolute;
    right: 50px;
    top: 638px;
    font-size: 14px;
    line-height: 1;
    font-weight: 700;
  }
  .promise {
    position: absolute;
    left: 0;
    top: 665px;
    width: 100%;
    text-align: center;
    font-size: 23px;
    font-weight: 700;
    font-style: italic;
    letter-spacing: 1.2px;
  }
  .author {
    position: absolute;
    right: 49px;
    top: 720px;
    font-size: 29px;
    line-height: 1;
    font-weight: 700;
  }
  .author-mark {
    position: absolute;
    left: 470px;
    top: 723px;
    width: 40px;
    height: 27px;
    background: var(--ink-white);
  }
</style>
</head>
<body>
  <main class="book-cover">
    <div class="cover-photo" role="img" aria-label="Photograph of a grandfather seated on a lawn in front of a porch, surrounded by his seven grandsons"></div>
    <h1 class="greeting">Hi Boys…………</h1>
    <p class="grandchildren">Owen&nbsp; | &nbsp;Daniel&nbsp; | &nbsp;Reid&nbsp; | &nbsp;Luke<br>Samuel&nbsp; | &nbsp;Henry&nbsp; | &nbsp;Thomas</p>
    <p class="tagline">There’s a turn in the path ahead……</p>
    <span class="title-lead">It’s called</span>
    <svg class="title-word" viewBox="0 0 215 80" role="img" aria-label="TIME">
      <text x="0" y="79" textLength="215" lengthAdjust="spacingAndGlyphs">TIME</text>
    </svg>
    <p class="title-aside">(and time won’t wait)</p>
    <p class="promise">This is about making it count.</p>
    <p class="author">Grandpa Hollis</p>
    <span class="author-mark" aria-hidden="true"></span>
  </main>
</body>
</html>
```